HUSH: Hush Until Stories Happen school library event

I need two poster designs for Hush Until Stories Happen (HUSH) in BC, requested by the PCSMG--Pacific Coast School Media Guild. One should be for elementary students and one for high school. I want the date (Monday, October 26, 2020) and Hush Until Stories Happen. I would like the posters in English and in French. French is : Ferme Ton Écran Maintenant! I'm including last year's posters as examples. I would like to be able to print the poster files on 11x17 paper.

• -The phrase "Hush Until Stories Happen" for the English version; "Ferme Ton Écran Maintenant" for the French version.
-Include the organization name: Pacific Coast School Media Guild
-The date: Monday, October 26, 2020
• I would like the elementary version to be bright and colourful--fun for younger kids. I would like the high school version to be a bit more mature for the older students. Can still be bright and colourful.

```html
<!DOCTYPE html>
<html lang="en">
<head>
<meta charset="utf-8">
<title>Hush Until Stories Happen – Poster</title>
<link rel="stylesheet" href="https://fonts.googleapis.com/css2?family=Bebas+Neue&family=Montserrat:wght@500&display=swap">
<style>
  :root {
    --stage: #3d3d3d;
    --paper: #ffffff;
    --sun: #fcce00;
    --sun-deep: #f2c000;
    --ink: #222222;
    --sky: #7dcfdc;
    --dots: #c9c9c9;
  }
  html, body {
    margin: 0;
    width: 1200px;
    height: 881px;
    overflow: hidden;
    background: var(--stage);
  }
  .poster {
    position: absolute;
    left: 328px;
    top: 20px;
    width: 543px;
    height: 840px;
    background: var(--paper);
    box-shadow: 0 4px 14px rgba(0,0,0,.35);
  }
  .poster svg { display: block; }
  .headline { font-family: "Bebas Neue", "Oswald", sans-serif; fill: var(--ink); }
  .headline-hero { font-family: "Bebas Neue", "Oswald", sans-serif; fill: var(--paper); }
  .headline-hero-shadow { font-family: "Bebas Neue", "Oswald", sans-serif; fill: var(--sun-deep); }
  .date { font-family: "Bebas Neue", "Oswald", sans-serif; fill: var(--paper); text-anchor: middle; }
  .org { font-family: "Montserrat", "Helvetica", sans-serif; font-weight: 500; fill: var(--ink); letter-spacing: 1px; }
</style>
</head>
<body>
<main class="poster">
  <svg viewBox="0 0 918 1421" width="543" height="840" role="img" aria-label="Hush Until Stories Happen poster, Monday October 26 2020">
    <rect class="paper" width="918" height="1421" fill="var(--paper)"/>

    <!-- sun disc -->
    <circle class="sun-disc" cx="274" cy="412" r="641" fill="var(--sun)"/>

    <!-- corner target -->
    <g class="corner-target">
      <circle cx="844" cy="78" r="52" fill="var(--paper)"/>
      <circle cx="844" cy="78" r="33" fill="none" stroke="var(--sky)" stroke-width="4"/>
      <circle cx="844" cy="78" r="13" fill="none" stroke="var(--sky)" stroke-width="4"/>
    </g>

    <!-- soft dot clusters -->
    <circle class="dot-cluster" cx="837" cy="838" r="60" fill="var(--dots)" opacity=".55" role="img" aria-label="halftone dot cluster"/>
    <circle class="dot-cluster" cx="499" cy="1418" r="62" fill="var(--dots)" opacity=".45" role="img" aria-label="halftone dot cluster"/>

    <!-- headline -->
    <g class="headline-stack">
      <text class="headline" x="50" y="197" font-size="200">HUSH</text>
      <text class="headline" x="50" y="362" font-size="200">UNTIL</text>
      <text class="headline" x="50" y="518" font-size="200">STORIES</text>
      <text class="headline-hero-shadow" x="66" y="882" font-size="470" textLength="660" lengthAdjust="spacingAndGlyphs">HAPPEN</text>
      <text class="headline-hero" x="46" y="870" font-size="470" textLength="660" lengthAdjust="spacingAndGlyphs">HAPPEN</text>
    </g>

    <!-- date bubble -->
    <g class="date-bubble">
      <circle cx="679" cy="1135" r="233" fill="var(--paper)" stroke="var(--sky)" stroke-width="4"/>
      <path d="M445 1040 A240 240 0 0 1 750 905" fill="none" stroke="var(--sun)" stroke-width="6"/>
      <polygon points="419,1263 505,1175 545,1262" fill="var(--sky)"/>
      <circle cx="677" cy="1133" r="197" fill="var(--sky)"/>
      <text class="date" x="677" y="1080" font-size="92">MONDAY</text>
      <text class="date" x="677" y="1163" font-size="96">OCTOBER 26</text>
      <text class="date" x="677" y="1245" font-size="92">2020</text>
    </g>

    <!-- small accents -->
    <circle class="accent-dot" cx="67" cy="1053" r="22" fill="var(--sky)"/>
    <g class="accent-target">
      <circle cx="349" cy="1157" r="24" fill="none" stroke="var(--sun)" stroke-width="3"/>
      <circle cx="349" cy="1157" r="9" fill="none" stroke="var(--sun)" stroke-width="3"/>
    </g>
    <rect class="dot-square" x="48" y="1123" width="96" height="96" fill="var(--dots)" opacity=".6" role="img" aria-label="halftone dot square"/>

    <!-- organisation -->
    <g class="org-name">
      <text class="org" x="48" y="1265" font-size="28">PACIFIC</text>
      <text class="org" x="48" y="1298" font-size="28">COAST</text>
      <text class="org" x="48" y="1331" font-size="28">SCHOOL MEDIA</text>
      <text class="org" x="48" y="1364" font-size="28">GUILD</text>
    </g>
  </svg>
</main>
</body>
</html>
```